Lumawerks Business Card Design

I need a business card design for a new Business, that is focused on Custom Made Designer Furniture. that is aimed at the mid to high end markets. I would like a card that would in some way portray what I do for my clients in the way we are able to make any idea a reality and also work within a set budget to meet their requirements.
I like quite contemporary colours and styling and I want the final design to communicate a Contemporary and Professional image.

Target Market(s)

mid to high end market

Industry/Entity Type

Business

Contact Information for Business Card

Lumawerks
Darren Holtzmann
18 Wexbury Rd, Kelston, Auckland, New Zealand 0712.

Requirements
Nice to have
• I would also like to utilize the spot gloss or raised print on my cards

```html
<!DOCTYPE html>
<html lang="en">
<head>
<meta charset="utf-8">
<title>Lumawerks Business Card</title>
<link rel="stylesheet" href="https://fonts.googleapis.com/css2?family=Inter:wght@100;200;800&display=swap">
<style>
  :root {
    --backdrop: #e6e4e1;
    --card-black: #050505;
    --accent-blue: #1ea6e3;
    --name-white: #f2f2f2;
    --pattern-tone: #d9d9d9;
  }
  * { margin: 0; padding: 0; box-sizing: border-box; }
  html, body {
    width: 1200px;
    height: 576px;
    overflow: hidden;
    background: var(--backdrop);
  }
  .canvas {
    position: relative;
    width: 1200px;
    height: 576px;
  }
  .business-card {
    position: absolute;
    left: 150px;
    top: 31px;
    width: 900px;
    height: 514px;
    background: var(--card-black);
    overflow: hidden;
    font-family: "Inter", "Helvetica Neue", Arial, sans-serif;
  }
  .edge-pattern {
    position: absolute;
    left: 0;
    top: 0;
    width: 112px;
    height: 410px;
    background: linear-gradient(180deg, #ffffff 0%, var(--pattern-tone) 100%);
  }
  .brand-name {
    position: absolute;
    left: 430px;
    top: 118px;
    color: var(--accent-blue);
    font-weight: 800;
    font-size: 34px;
    letter-spacing: -0.5px;
  }
  .person-name {
    position: absolute;
    left: 225px;
    top: 186px;
    color: var(--name-white);
    font-weight: 100;
    font-size: 72px;
    letter-spacing: -1px;
    white-space: nowrap;
  }
  .address {
    position: absolute;
    left: 330px;
    top: 320px;
    color: var(--accent-blue);
    font-weight: 800;
    font-size: 22px;
    line-height: 1.3;
    font-style: normal;
  }
  .address span { display: block; }
  .address .address-line-2 { padding-left: 40px; }
</style>
</head>
<body>
  <main class="canvas">
    <section class="business-card" aria-label="Lumawerks business card">
      <div class="edge-pattern" role="img" aria-label="White interlocking line pattern running down the left edge of the card"></div>
      <p class="brand-name">Lumawerks</p>
      <h1 class="person-name">Darren Holtzmann</h1>
      <address class="address">
        <span class="address-line-1">18 Wexbury Rd, Kelston, Auckland</span>
        <span class="address-line-2">New Zealand 0712</span>
      </address>
    </section>
  </main>
</body>
</html>
```